Home Design company focused on remodel and enhancement of kitchens and bathroorms

I already have a logo designed by ArtHarbor, I now need a design for my business cards.
The company is in the remodeling and enhancement industry for homes, focusing on kitchens and bathrooms, however, we can remodel or enhance every room in a home, an office space, etc.

The company's name is VELMOR HOME DESIGN, LLC

We'll focus on clients in the Rio Grande Valley, Texas. Primarily McAllen, Edinburg, Pharr, Mission, Brownsville and South Padre Island.

The design on the business card should transmit reliability, professionalism anda bit of upscale design.

The logo is in black and white, and would like to keep it that way.

The information that needs to be printed in the business cards is:
Company's name: Velmor Home Design
Company's Logo (attached)
My name: Noel Bramwit
Address, phone and email:
2715 N Parkline Road, Ste 348
Corvale, TX 70000
(555) 555 0187
nbramwit@velmordesign.example
Website: velmordesign.example

```html
<!DOCTYPE html>
<html lang="en">
<head>
<meta charset="utf-8">
<title>Velmor Home Design – Business Cards</title>
<link href="https://fonts.googleapis.com/css2?family=Montserrat:wght@300;800&family=Roboto:wght@400&display=swap" rel="stylesheet">
<style>
  :root {
    --ink: #0b0b0b;
    --paper: #f4f4f2;
    --silver: #b9b9b9;
    --backdrop: #d9d9d9;
  }
  html, body {
    margin: 0;
    width: 1200px;
    height: 1200px;
    overflow: hidden;
    background: var(--backdrop);
  }
  .sheet {
    position: relative;
    width: 1200px;
    height: 1200px;
  }
  .card {
    position: absolute;
    left: 250px;
    width: 700px;
    height: 400px;
    background: var(--ink);
    overflow: hidden;
    box-shadow: 0 10px 30px rgba(0,0,0,.25);
  }
  .card--front { top: 150px; }
  .card--back { top: 650px; }
  .card svg.shapes {
    position: absolute;
    inset: 0;
  }
  .brand {
    position: absolute;
    display: flex;
    align-items: center;
    gap: 12px;
    font-family: "Montserrat", sans-serif;
    font-weight: 300;
    letter-spacing: 0.28em;
    text-transform: uppercase;
  }
  .brand__mark {
    width: 14px;
    height: 14px;
    background: currentColor;
  }
  .brand__name { font-size: 14px; line-height: 1.35; }
  .card--front .brand {
    left: 100px;
    top: 178px;
    color: var(--paper);
  }
  .card--back .brand {
    left: 0;
    right: 0;
    top: 178px;
    justify-content: center;
    color: var(--silver);
  }
  .card--back .brand__name { font-size: 17px; }
  .contact {
    position: absolute;
    left: 440px;
    top: 78px;
    color: var(--ink);
    font-family: "Roboto", sans-serif;
  }
  .contact__name {
    margin: 0 0 26px;
    font-family: "Montserrat", sans-serif;
    font-weight: 800;
    font-size: 27px;
    letter-spacing: 0.02em;
    text-transform: uppercase;
  }
  .contact__list {
    list-style: none;
    margin: 0;
    padding: 0;
    font-size: 13px;
  }
  .contact__list li {
    display: flex;
    align-items: center;
    gap: 8px;
    margin-bottom: 7px;
  }
  .contact__list svg { width: 13px; height: 13px; flex: none; }
  .address {
    position: absolute;
    left: 458px;
    top: 236px;
    display: flex;
    align-items: center;
    gap: 9px;
    color: var(--paper);
    font-family: "Roboto", sans-serif;
    font-size: 13px;
    line-height: 1.3;
  }
  .address svg { width: 13px; height: 16px; flex: none; }
</style>
</head>
<body>
<main class="sheet">

  <section class="card card--front" aria-label="Business card front">
    <svg class="shapes" viewBox="0 0 700 400" width="700" height="400" aria-hidden="true">
      <polygon points="350,0 700,0 700,400 520,400 460,300 420,130" fill="var(--paper)"/>
      <polygon points="470,232 700,232 700,292 440,292 410,262" fill="var(--ink)"/>
      <polygon points="500,292 700,292 700,320 560,400 520,400" fill="var(--paper)"/>
      <polygon points="80,0 96,0 56,400 40,400" fill="var(--paper)"/>
      <polygon points="262,0 278,0 248,300 232,300" fill="var(--paper)"/>
    </svg>
    <div class="brand">
      <span class="brand__mark"></span>
      <span class="brand__name">Velmor<br>Home<br>Design</span>
    </div>
    <div class="contact">
      <h1 class="contact__name">Noel Bramwit</h1>
      <ul class="contact__list">
        <li>
          <svg viewBox="0 0 24 24"><path fill="currentColor" d="M6.6 10.8a15 15 0 0 0 6.6 6.6l2.2-2.2c.3-.3.7-.4 1-.2 1.1.4 2.3.6 3.6.6.6 0 1 .4 1 1V20c0 .6-.4 1-1 1A17 17 0 0 1 3 4c0-.6.4-1 1-1h3.5c.6 0 1 .4 1 1 0 1.3.2 2.5.6 3.6.1.3 0 .7-.2 1z"/></svg>
          (555) 555 0187
        </li>
        <li>
          <svg viewBox="0 0 24 24"><circle cx="12" cy="12" r="10" fill="none" stroke="currentColor" stroke-width="2"/><path d="M2 12h20M12 2c3 3 3 17 0 20M12 2c-3 3-3 17 0 20" fill="none" stroke="currentColor" stroke-width="2"/></svg>
          www.velmordesign.example
        </li>
        <li>
          <svg viewBox="0 0 24 24"><rect x="2" y="5" width="20" height="14" fill="currentColor"/><path d="M2 5l10 8 10-8" fill="none" stroke="var(--paper)" stroke-width="1.6"/></svg>
          nbramwit@velmordesign.example
        </li>
      </ul>
    </div>
    <div class="address">
      <svg viewBox="0 0 24 30"><path fill="currentColor" d="M12 0a10 10 0 0 0-10 10c0 8 10 20 10 20s10-12 10-20A10 10 0 0 0 12 0zm0 14a4 4 0 1 1 0-8 4 4 0 0 1 0 8z"/></svg>
      <span>2715 N Parkline Road, Ste 348<br>Corvale, TX 70000</span>
    </div>
  </section>

  <section class="card card--back" aria-label="Business card back">
    <svg class="shapes" viewBox="0 0 700 400" width="700" height="400" aria-hidden="true">
      <polygon points="185,0 201,0 186,130 170,130" fill="var(--paper)"/>
      <polygon points="155,280 171,280 157,400 141,400" fill="var(--paper)"/>
      <polygon points="520,0 536,0 524,110 508,110" fill="var(--paper)"/>
      <polygon points="500,270 516,270 500,400 484,400" fill="var(--paper)"/>
    </svg>
    <div class="brand">
      <span class="brand__mark"></span>
      <span class="brand__name">Velmor<br>Home<br>Design</span>
    </div>
  </section>

</main>
</body>
</html>
```